Industrial design for commercialization of products for cargo

Good morning, we need a website design divided into 4 sections for a newly created company. Torvelix means Industrial Products for Loading and Pumping. We are located in the capital of Mexico and distributed throughout the country. We sell a wide range of equipment and accessories, for handling and lifting of load: hoists, traction devices, trolleys, pulleys, cables, shackles, tensioners, rings, marine chains, among others, as well as pneumatic double diaphragm pumps And centrifugal pumps, used in the pharmaceutical, chemical, food, etc. industries. Our products are manufactured to the highest quality standards, most are manufactured in the United States. Recently, Artmosaic Hub (KALT.MERON) produced our company logo and we would like our website to be combined with it. We want the website to have an industrial design, that the colors combine with the logo and black letters. The images and information that we will use are in our current web page: www.torvelix-demo.com. If you need more information, please let us know. My name is Lidia Quevara and my email is ventastorvelix@mailbox-demo.net. Thank you. PD Please, I want the winner to upload to my server, the coded files html and CSS through FTP (File Transfer Protocol) I know this action means an extra cost, but I m willing to pay. Thanks.
Target Market(s)
Our market is very broad, among our clients are companies in the construction industry, manufacturing, as well as department stores, warehouses, even shops, seaports.
Industry/Entity Type
Commercial
Coding
Coded - Design and coding required
Number of Pages Required
5+ page
Font styles to use
Other font styles liked:
- Hay libertad en cuanto a la tipografía, pueden utilizar la que ustedes consideren conveniente.

Colors
Designer to choose colors to be used in the design.
Requirements
Must have
- The page that we want should be divided into the sections that you consider convenient. SECTION OF HOME INFORMATION.- Our data, biography, mission, vision, values, company address, telephone number, whatsapp, email and location map. PRODUCTS FOR LOADING. PRODUCTS FOR PUMPING. ACCESSORIES FOR LOADING. CONTACT.

Nice to have
- One design you can use as an example is the page of one of our suppliers: www.vultenor.com.mx, we would like our page to be better than that of this provider. We want you to have a better presentation. I would like them to use banners at the top and bottom where phone numbers are placed. I wish there was a space for the videos to run the products. My page must be in the Spanish language please. The choice of colors is at your discretion, however instead of the color orange, I would like them to use the color red.

Should not have
- My project should not seem unprofessional, but to show that we are a serious and important company. Do not look anything like our current page www.torvelix-demo.com We do not want the option to add to the shopping cart or a page with a catalog. Our page is just a means to promote our products. Sales are done by phone.

```html
<!DOCTYPE html>
<html lang="en">
<head>
<meta charset="utf-8">
<title>Torvelix — Industrial Products for Loading and Pumping</title>
<link href="https://fonts.googleapis.com/css2?family=Open+Sans:wght@400;600;700;800&display=swap" rel="stylesheet">
<style>
:root{
  --red:#d9412b;
  --red-dark:#b8321f;
  --ink:#222;
  --text:#555;
  --muted:#888;
  --nav:#2b2b2b;
  --nav-deep:#1f1f1f;
  --grey-bg:#f1f1f1;
  --line:#dcdcdc;
  --white:#fff;
  --black:#0d0d0d;
}
*{box-sizing:border-box;margin:0;padding:0}
html,body{width:1200px;height:2584px;overflow:hidden}
body{font-family:"Open Sans",Arial,sans-serif;color:var(--ink);background:var(--white);position:relative}
.brand{display:flex;align-items:center;gap:12px}
.brand-mark{width:34px;height:34px;background:var(--red)}
.brand-name{font-weight:800;font-size:26px;color:var(--red);letter-spacing:1px}

/* top header */
.topbar{height:92px;display:flex;align-items:center;justify-content:space-between;padding:0 80px}
.contacts{display:flex;gap:38px}
.contact{display:flex;align-items:center;gap:10px}
.contact-icon{width:36px;height:36px;border-radius:50%;background:var(--red);display:flex;align-items:center;justify-content:center}
.contact-label{font-size:11px;font-weight:700;color:var(--ink)}
.contact-value{font-size:15px;font-weight:700;color:var(--red)}
.contact-value.small{font-size:11px;font-weight:600;color:var(--text);line-height:1.3}

/* nav */
.mainnav{height:48px;background:var(--nav);display:flex;align-items:center;justify-content:space-between;padding:0 80px 0 80px}
.mainnav ul{list-style:none;display:flex;height:100%}
.mainnav li{height:100%;display:flex;align-items:center;padding:0 22px;font-size:13px;font-weight:700;color:var(--white)}
.mainnav li.active{background:var(--red)}

/* hero */
.hero{position:relative;height:520px;background:linear-gradient(110deg,#c9cbcd 0%,#8e9499 35%,#5d6368 60%,#a4a8ab 100%)}
.hero-photo{position:absolute;inset:0;background:radial-gradient(ellipse 180px 240px at 640px 300px,rgba(232,190,40,.85),rgba(232,190,40,0) 70%),linear-gradient(90deg,rgba(40,40,40,.25),rgba(255,255,255,0) 50%,rgba(40,40,40,.2))}
.hero-copy{position:absolute;left:40px;top:150px}
.hero-title{display:inline-block;background:var(--red);color:var(--white);font-weight:700;font-size:30px;padding:8px 18px;letter-spacing:1px}
.hero-sub{margin-top:4px;background:rgba(217,65,43,.82);color:var(--white);font-weight:700;font-size:19px;line-height:1.3;padding:8px 18px;width:420px}
.hero-arrow{position:absolute;top:240px;width:36px;height:48px;background:rgba(255,255,255,.55);display:flex;align-items:center;justify-content:center}
.hero-arrow.left{left:0}.hero-arrow.right{right:0}
.hero-dots{position:absolute;bottom:16px;left:50%;transform:translateX(-50%);display:flex;gap:8px}
.hero-dots span{width:10px;height:10px;border-radius:50%;background:rgba(255,255,255,.6)}
.hero-dots span.on{background:var(--nav)}

/* section headings */
.section-title{text-align:center;font-size:26px;font-weight:700;color:var(--ink);letter-spacing:.5px}
.section-rule{width:44px;height:3px;background:var(--red);margin:10px auto 0}

/* welcome */
.welcome{height:290px;padding-top:70px;text-align:center}
.welcome p{width:880px;margin:30px auto 0;font-size:13px;line-height:1.6;color:var(--text)}
.btn{display:inline-block;background:var(--red);color:var(--white);font-size:13px;font-weight:700;padding:11px 26px;letter-spacing:.5px}
.welcome .btn{margin-top:26px}

/* products */
.products{height:770px;background:var(--grey-bg);padding-top:60px}
.product-grid{display:grid;grid-template-columns:repeat(4,240px);gap:30px 26px;justify-content:center;margin-top:34px}
.product{background:var(--white);border:1px solid var(--line)}
.product-photo{height:214px}
.product-label{height:36px;background:var(--nav);color:var(--white);font-size:13px;font-weight:700;display:flex;align-items:center;justify-content:center}
.ph-pump{background:linear-gradient(160deg,#f4f4f4,#9fa3a6 55%,#e9e9e9)}
.ph-yellow{background:radial-gradient(circle at 50% 45%,#e3b830 0,#f6f6f6 46%)}
.ph-black{background:radial-gradient(circle at 50% 45%,#3a3a3a 0,#f6f6f6 50%)}
.ph-blue{background:radial-gradient(circle at 50% 45%,#2e5fa8 0,#f6f6f6 50%)}
.ph-red{background:radial-gradient(circle at 50% 45%,#c8352a 0,#f6f6f6 50%)}
.ph-orange{background:radial-gradient(circle at 50% 45%,#e06a2c 0,#f6f6f6 50%)}
.products .cta{text-align:center;margin-top:36px}

/* distributors */
.distributors{height:400px;padding-top:40px;position:relative}
.partner-grid{display:grid;grid-template-columns:repeat(4,240px);gap:30px 26px;justify-content:center;margin-top:36px}
.partner{height:100px;border:1px solid var(--line);display:flex;align-items:center;justify-content:center;font-size:24px;font-weight:800;color:var(--ink)}
.partner-arrow{position:absolute;top:220px;width:20px;height:40px;display:flex;align-items:center;justify-content:center}
.partner-arrow.left{left:40px}.partner-arrow.right{right:40px}

/* newsletter */
.newsletter{height:240px;background:var(--black);text-align:center;padding-top:48px;color:var(--white)}
.newsletter h2{font-size:26px;font-weight:700;letter-spacing:.5px}
.newsletter p{font-size:13px;color:#bdbdbd;margin-top:10px}
.signup{display:flex;justify-content:center;margin-top:26px;gap:10px}
.signup .field{width:400px;height:40px;background:var(--white);color:var(--muted);font-size:12px;display:flex;align-items:center;padding-left:14px}
.signup .btn{height:40px;padding:0 26px;display:flex;align-items:center}

/* footer */
.footer{height:224px;display:grid;grid-template-columns:260px 220px 320px 220px;gap:20px;padding:40px 80px 0}
.footer .copy{font-size:11px;color:var(--muted);margin-top:14px;line-height:1.5}
.footer h3{font-size:13px;font-weight:700;color:var(--red);margin-bottom:10px}
.sitemap{display:grid;grid-template-columns:1fr 1fr;font-size:12px;color:var(--text);line-height:1.8}
.contact-info{font-size:12px;color:var(--text);line-height:1.6}
.contact-info strong{color:var(--ink);font-size:11px}
.social{display:flex;gap:12px}
.social span{width:22px;height:22px;background:#9a9a9a;border-radius:3px}
.footer .credit{position:absolute;right:30px;bottom:18px;font-size:10px;color:var(--muted)}
</style>
</head>
<body>

<header class="topbar">
  <div class="brand"><span class="brand-mark"></span><span class="brand-name">TORVELIX</span></div>
  <div class="contacts">
    <div class="contact">
      <span class="contact-icon"><svg width="18" height="18" viewBox="0 0 24 24"><path fill="#fff" d="M6.6 10.8a15 15 0 0 0 6.6 6.6l2.2-2.2c.3-.3.7-.4 1-.2 1.1.4 2.3.6 3.6.6.6 0 1 .4 1 1V20c0 .6-.4 1-1 1A17 17 0 0 1 3 4c0-.6.4-1 1-1h3.5c.6 0 1 .4 1 1 0 1.3.2 2.5.6 3.6.1.3 0 .7-.2 1z"/></svg></span>
      <div><div class="contact-label">CALL:</div><div class="contact-value">01 55 4210 7386</div></div>
    </div>
    <div class="contact">
      <span class="contact-icon"><svg width="18" height="18" viewBox="0 0 24 24"><path fill="#fff" d="M4 4h16v12H8l-4 4z"/></svg></span>
      <div><div class="contact-label">WHATSAPP:</div><div class="contact-value">55 3170 6429</div></div>
    </div>
    <div class="contact">
      <span class="contact-icon"><svg width="18" height="18" viewBox="0 0 24 24"><path fill="#fff" d="M3 5h18v14H3z"/><path d="M3 5l9 7 9-7" stroke="#d9412b" stroke-width="2" fill="none"/></svg></span>
      <div><div class="contact-label">EMAIL:</div><div class="contact-value small">ventastorvelix@mailbox-demo.net<br>info@torvelix-demo.com</div></div>
    </div>
  </div>
</header>

<nav class="mainnav">
  <ul>
    <li class="active">HOME</li><li>INFORMATION</li><li>LOADING</li><li>PUMPING</li><li>ACCESSORIES</li><li>CONTACT</li>
  </ul>
  <svg width="18" height="18" viewBox="0 0 24 24"><circle cx="10" cy="10" r="6.5" stroke="#fff" stroke-width="2.5" fill="none"/><path d="M15 15l6 6" stroke="#fff" stroke-width="2.5"/></svg>
</nav>

<section class="hero">
  <div class="hero-photo" role="img" aria-label="Yellow lifting hook hanging from a heavy chain hoist in a workshop"></div>
  <div class="hero-copy">
    <div class="hero-title">WELCOME TO TORVELIX</div>
    <div class="hero-sub">We sell a wide range of equipment and accessories, for handling and lifting of load</div>
  </div>
  <div class="hero-arrow left"><svg width="14" height="20" viewBox="0 0 14 20"><path d="M11 2L3 10l8 8" stroke="#fff" stroke-width="3" fill="none"/></svg></div>
  <div class="hero-arrow right"><svg width="14" height="20" viewBox="0 0 14 20"><path d="M3 2l8 8-8 8" stroke="#fff" stroke-width="3" fill="none"/></svg></div>
  <div class="hero-dots"><span class="on"></span><span></span><span></span><span></span></div>
</section>

<section class="welcome">
  <h2 class="section-title">WELCOME TO OUR WEBSITE</h2>
  <div class="section-rule"></div>
  <p>TORVELIX Industrial Products For Loading and Pumping. We are a company dedicated to selling products for cargo: VARNHOLT, BRENLIFT and QUENMAR, manufactured in the USA and Mexico, with the highest quality standards; Norvane Brand Chain and Polyester Lanyards and Loading Accessories Brand Halvik.</p>
  <span class="btn">READ MORE</span>
</section>

<section class="products">
  <h2 class="section-title">OUR PRODUCTS</h2>
  <div class="section-rule"></div>
  <div class="product-grid">
    <div class="product"><div class="product-photo ph-pump" role="img" aria-label="Stainless steel centrifugal pump"></div><div class="product-label">CENTRIFUGAL PUMPS</div></div>
    <div class="product"><div class="product-photo ph-yellow" role="img" aria-label="Yellow lever chain hoist"></div><div class="product-label">HOISTS</div></div>
    <div class="product"><div class="product-photo ph-black" role="img" aria-label="Electric chain hoist"></div><div class="product-label">HOISTS</div></div>
    <div class="product"><div class="product-photo ph-blue" role="img" aria-label="Blue electric wire rope hoist"></div><div class="product-label">HOISTS</div></div>
    <div class="product"><div class="product-photo ph-black" role="img" aria-label="Air powered hoist"></div><div class="product-label">HOISTS</div></div>
    <div class="product"><div class="product-photo ph-red" role="img" aria-label="Red manual chain hoist"></div><div class="product-label">HOISTS</div></div>
    <div class="product"><div class="product-photo ph-orange" role="img" aria-label="Double diaphragm pump"></div><div class="product-label">HOISTS</div></div>
    <div class="product"><div class="product-photo ph-red" role="img" aria-label="Red pneumatic winch"></div><div class="product-label">HOISTS</div></div>
  </div>
  <div class="cta"><span class="btn">VIEW ALL PRODUCTS</span></div>
</section>

<section class="distributors">
  <h2 class="section-title">WE ARE AUTHORIZED DISTRIBUTORS</h2>
  <div class="section-rule"></div>
  <div class="partner-grid">
    <div class="partner">Halvik</div>
    <div class="partner">Ostrevo</div>
    <div class="partner">Varnholt</div>
    <div class="partner">Quenmar</div>
    <div class="partner">Pelrano</div>
    <div class="partner">Norvane</div>
    <div class="partner">Draxmoor</div>
    <div class="partner">Tesquil</div>
  </div>
  <div class="partner-arrow left"><svg width="12" height="20" viewBox="0 0 12 20"><path d="M10 2L2 10l8 8" stroke="#999" stroke-width="2.5" fill="none"/></svg></div>
  <div class="partner-arrow right"><svg width="12" height="20" viewBox="0 0 12 20"><path d="M2 2l8 8-8 8" stroke="#999" stroke-width="2.5" fill="none"/></svg></div>
</section>

<section class="newsletter">
  <h2>NEWSLETTER SIGN UP</h2>
  <p>Lorem ipsum dolor sit amet, consectetuer adipiscing elit, sed diam nonummy nibh euismod</p>
  <div class="signup"><span class="field">Enter Email Address</span><span class="btn">SIGN UP</span></div>
</section>

<footer class="footer">
  <div>
    <div class="brand"><span class="brand-mark"></span><span class="brand-name">TORVELIX</span></div>
    <p class="copy">Copyright © 2013 Company Name<br>All Rights Reserved</p>
  </div>
  <div>
    <h3>SITE MAP</h3>
    <div class="sitemap"><span>Home</span><span>Accessories</span><span>Information</span><span>Contact us</span><span>Loading</span><span></span><span>Pumping</span></div>
  </div>
  <div>
    <h3>CONTACT INFO</h3>
    <div class="contact-info"><strong>ADMINISTRATIVE OFFICE</strong><br>Calle Ferrando 27 interior 3,<br>Col. Prado Norte,<br>Delegación Miguel Hidalgo,<br>Mexico City</div>
  </div>
  <div>
    <h3>FOLLOW US</h3>
    <div class="social"><span></span><span></span><span></span><span></span><span></span></div>
  </div>
</footer>

</body>
</html>
```